CedarBight.Lawyer, a new website for Morris.

Looking for a professional web site for my small country law firm.
I have a logo, chart, map, my photo, office photo, google analytics code, my drone video on YouTube, "Brantwell Beacon Skyrun, also on www.loftcove.guide", and text content. I am figuring out how to get those into digital forms.
First page needs a professional look. Here's where I am really hoping for your skill set.
Banner should be well designed so as to "ease" the viewer into confidence in my firm
Prefer the "white backround", less cluttered style of design.
My office has been in Key Center, main and only town of Key Peninsula, for 25 years, with emphasis on real property matters. Naturally land lasts longer than people, so estates, trusts and succession issues are relevant.
Local KP is the heart of southern Puget Sound, 75 miles of spectacular residential waterfront. We have the best land, waterfront, beaches and views in Puget Sound, however of course Seattle and the San Juan Islands could not be disregarded. It's that we have the most privacy, the best old growth Doug Firs, wildlife and low population density.
Puget Sound conditions are very specific for residential development.
One must consider:
Topography, hydro-geology, geomorphology, hill slope stability, soils must support septic systems, individual wells, prescriptive, express and implied easement issues, boundary lines don't always line up with surveys or expectations, or historic use, thus adverse possession abounds environmentally protected shorelines and wetlands, all challenges, but ohh.., the views and unique, world class waterfront.
Everyone who lives on Puget Sound is convinced they live in the most beautiful and spectacular place in the world, and we're all correct.

Target Market(s)

Members of the Halvern-Ostrow County Bar Association, and more distant counsel seeking consultation re: local conditions.
Also, I decided it was time to have a website, so a reference place to direct clients.
I like the professional sound of .lawyer vs. commercial sound of .com.

Industry/Entity Type

Law Firm

Coding

Coded - Design and coding required

Number of Pages Required

5+ page

Font styles to use
Other font styles liked:
• That newly created "web" font everyone seems to be usIng

Colors
32b8a4
3377b5

Requirements
Must have
• A strong first page with my photo and Puget Sound chart professionally created.
• A page I have ready with local links.
• A "How to find me page", which should have a map, and photo of my office, which I can make with the preloaded templates the host provides.
• A "This is what I do page", with some testimonials, which I can do via said templates or preferably by professionals.
Nice to have
• Clean look.
• Consistent looks to pages.
• First comment I got back talked about just designing one page, and if requires $340.00, so be it.
• Typical local sites have 4/5 pages, so perhaps a "fill-able" generic pages, I can build myself.
• Ideally, I would step into a working site I can edit myself.
• Not looking for e-commerce site, but the remainder of language the "Smart" professional used is unknown to me.
• Bit out of my element here, hoping for guidance.
Should not have
• Clutter

```html
<!DOCTYPE html>
<html lang="en">
<head>
<meta charset="utf-8">
<title>CedarBight.Lawyer — Homepage</title>
<link href="https://fonts.googleapis.com/css2?family=Exo+2:wght@300;400;500&family=Tinos&display=swap" rel="stylesheet">
<style>
:root{
  --page:#e1e5e8;
  --navy:#2d3a4c;
  --accent:#3377b5;
  --white:#ffffff;
  --text:#6b7179;
  --heading:#3d4550;
  --name:#4a7aab;
  --icon-bg:#c9ced3;
  --field:#f6f7f8;
  --field-line:#d3d7db;
  --quote:#cfd4d9;
}
*{box-sizing:border-box;margin:0;padding:0}
html,body{width:721px;height:1200px;overflow:hidden}
body{background:var(--page);font-family:"Exo 2",sans-serif;color:var(--text);position:relative}
.abs{position:absolute}
a{text-decoration:none}

.topbar-phone{left:522px;top:8px;font-size:13px;color:#4a4f57;font-weight:300;display:flex;align-items:center;gap:3px}
.topbar-divider{left:632px;top:9px;width:1px;height:17px;background:#c6cbd0}
.social-dot{width:13px;height:13px;border-radius:50%;background:#b9bfc5}

.site-header{left:40px;top:35px;width:641px;height:42px;background:var(--navy)}
.brand{left:40px;top:35px;width:148px;height:70px;background:var(--white);display:flex;align-items:center;justify-content:center;gap:5px;z-index:3}
.brand-mark{width:20px;height:20px;border-radius:50%;background:#2f3f9a}
.brand-name{font-size:12.5px;font-weight:500;color:#2f3f9a}
.main-nav{right:40px;top:35px;height:42px;display:flex;z-index:2}
.main-nav a{display:flex;align-items:center;padding:0 10px;font-size:8px;color:var(--white);text-transform:uppercase}
.main-nav a.active{background:var(--accent);padding:0 11px}

.hero{left:0;top:77px;width:721px;height:268px;background:linear-gradient(180deg,#1f3a5e 0%,#35618e 25%,#5a88ab 45%,#8f9fac 58%,#c98a6a 70%,#e2643e 80%,#7e3a34 90%,#2a2c38 100%)}
.hero-caption{left:114px;top:193px;height:36px;padding:0 11px;background:rgba(40,48,140,.85);color:var(--white);font-family:"Tinos",serif;font-size:25px;display:flex;align-items:center}
.hero-shadow{left:20px;top:345px;width:681px;height:14px;background:radial-gradient(ellipse at top,rgba(0,0,0,.35),rgba(0,0,0,0) 70%)}

.feature{top:359px;width:214px;height:270px;background:var(--white)}
.feature-photo{height:142px;border-bottom:2px solid #9fa6ad}
.feature h2{font-weight:300;font-size:13px;color:var(--heading);margin:10px 11px 8px;text-transform:uppercase}
.feature p{font-size:7.4px;line-height:11px;margin:0 18px 0 11px;font-weight:300}
.feature .more{display:block;text-align:right;font-size:7.5px;color:var(--heading);margin:7px 11px 0}

.team-card{top:642px;width:214px;text-align:center}
.team-photo{height:173px}
.team-name{font-size:10.5px;color:var(--name);margin-top:6px;font-weight:300}
.team-role{font-size:7.5px;color:var(--text);margin-top:1px;font-weight:300}
.team-links{display:flex;justify-content:center;gap:3px;margin-top:5px}
.team-links span{width:14px;height:14px;border-radius:50%;background:#b4bac0;display:flex;align-items:center;justify-content:center}

.rule{left:45px;top:876px;width:641px;height:1px;background:#cdd2d6}

.section-title{top:896px;font-size:13.5px;font-weight:300;color:var(--heading);text-transform:uppercase}
.quote-link{left:230px;top:896px;width:17px;height:16px;background:var(--white);display:flex;align-items:center;justify-content:center}
.quote{left:56px;top:921px;width:191px;height:54px;background:var(--quote);font-size:7.3px;line-height:11px;padding:8px 10px;font-weight:300}
.quote-tail{left:84px;top:975px;width:0;height:0;border-left:12px solid transparent;border-right:12px solid transparent;border-top:12px solid var(--quote)}
.client-photo{left:74px;top:997px;width:39px;height:38px;background:linear-gradient(180deg,#c7c9c8,#8b8f92);border:1px solid var(--white)}
.client-name{left:121px;top:1000px;font-size:8.5px;color:var(--name);font-weight:300}
.client-org{left:121px;top:1011px;font-size:7.5px;font-weight:300}
.quote-arrows{left:212px;top:1029px;width:35px;height:17px;background:var(--white);display:flex}
.quote-arrows span{flex:1;display:flex;align-items:center;justify-content:center}

.contact-row{left:269px;display:flex;align-items:flex-start;gap:6px;font-size:7.5px;color:#4f5660;text-transform:uppercase;font-weight:300}
.contact-icon{width:27px;height:27px;background:var(--icon-bg);display:flex;align-items:center;justify-content:center}
.contact-row span{padding-top:4px}

.field{left:483px;width:192px;height:18px;background:var(--field);border:1px solid var(--field-line);font-size:7px;padding:0 6px;display:flex;align-items:center;color:#777}
.message-box{left:483px;top:999px;width:192px;height:65px;background:var(--field);border:1px solid var(--field-line)}
.send-btn{left:604px;top:1071px;width:71px;height:17px;background:linear-gradient(180deg,#5a93c9,#3377b5);color:var(--white);font-size:7.5px;display:flex;align-items:center;justify-content:center}

.site-footer{left:0;top:1118px;width:721px;height:82px;background:var(--navy)}
.footer-rule{left:45px;top:1161px;width:641px;height:1px;background:#3b4859}
.copyright{left:45px;top:1174px;font-size:6.5px;color:#6e7a89}
</style>
</head>
<body>

<div class="abs topbar-phone">
  <svg width="7" height="10" viewBox="0 0 7 10"><rect x=".5" y=".5" width="6" height="9" rx="1" fill="none" stroke="#b9bfc5"/></svg>
  -555-3140-772
</div>
<div class="abs topbar-divider"></div>
<div class="abs social-dot" style="left:644px;top:10px"></div>
<div class="abs social-dot" style="left:665px;top:10px"></div>

<div class="abs site-header"></div>
<div class="abs brand"><span class="brand-mark"></span><span class="brand-name">CedarBight.Lawyer</span></div>
<nav class="abs main-nav">
  <a class="active" href="#">Homepage</a><a href="#">About</a><a href="#">Services</a><a href="#">Contacts</a>
</nav>

<div class="abs hero" role="img" aria-label="Sunset sky over the sound with fir silhouette"></div>
<div class="abs hero-caption">Lorem ipsum dolor</div>
<div class="abs hero-shadow"></div>

<section class="abs feature" style="left:45px">
  <div class="feature-photo" role="img" aria-label="Handshake between two business people" style="background:linear-gradient(135deg,#8ea3ba,#dde4ea 55%,#4f6378)"></div>
  <h2>Welcome</h2>
  <p>Lorem ipsum dolor sit amet consectetur adipiscing elit sed do eiusmod tempor incididunt ut labore et dolore magna aliqua Ut enim ad minim veniam quis nostrud exercitation ullamco laboris nisi ut aliquip ex commodo consequat Duis aute irure dolor in reprehenderit in voluptate velit esse cillum dolore eu fugiat nulla pariatur.</p>
  <a class="more" href="#">Read more ›</a>
</section>
<section class="abs feature" style="left:259px;background:#eceef0">
  <div class="feature-photo" role="img" aria-label="Man in shirt and tie holding gears" style="background:linear-gradient(90deg,#9aa8b8,#6f8fb8 50%,#2a2d33)"></div>
  <h2>Our Practice Areas</h2>
  <p>Lorem ipsum dolor sit amet consectetur adipiscing elit sed do eiusmod tempor incididunt ut labore et dolore magna aliqua Ut enim ad minim veniam quis nostrud exercitation ullamco laboris nisi ut aliquip ex commodo consequat Duis aute irure dolor in reprehenderit in voluptate velit esse cillum dolore eu fugiat nulla pariatur.</p>
  <a class="more" href="#">Read more ›</a>
</section>
<section class="abs feature" style="left:472px">
  <div class="feature-photo" role="img" aria-label="Pen resting on a leather notebook" style="background:linear-gradient(135deg,#3a2320,#7a3b33 50%,#5a2c27)"></div>
  <h2>About Us</h2>
  <p>Lorem ipsum dolor sit amet consectetur adipiscing elit sed do eiusmod tempor incididunt ut labore et dolore magna aliqua Ut enim ad minim veniam quis nostrud exercitation ullamco laboris nisi ut aliquip ex commodo consequat Duis aute irure dolor in reprehenderit in voluptate velit esse cillum dolore eu fugiat nulla pariatur.</p>
  <a class="more" href="#">Read more ›</a>
</section>

<div class="abs team-card" style="left:45px">
  <div class="team-photo" role="img" aria-label="Portrait of team member Jon Doe" style="background:linear-gradient(180deg,#c9cacb,#8d9092)"></div>
  <div class="team-name">JON DOE</div><div class="team-role">Director</div>
  <div class="team-links"><span><svg width="8" height="6" viewBox="0 0 8 6"><rect width="8" height="6" fill="#fff"/><path d="M0 0l4 3 4-3" stroke="#b4bac0" fill="none"/></svg></span><span></span><span></span></div>
</div>
<div class="abs team-card" style="left:259px">
  <div class="team-photo" role="img" aria-label="Portrait of team member Robert Green" style="background:linear-gradient(180deg,#b9bcbd,#8a8d8f)"></div>
  <div class="team-name">ROBERT GREEN</div><div class="team-role">Manager</div>
  <div class="team-links"><span><svg width="8" height="6" viewBox="0 0 8 6"><rect width="8" height="6" fill="#fff"/><path d="M0 0l4 3 4-3" stroke="#b4bac0" fill="none"/></svg></span><span></span><span></span></div>
</div>
<div class="abs team-card" style="left:472px">
  <div class="team-photo" role="img" aria-label="Portrait of team member Martin Brown" style="background:linear-gradient(180deg,#cfcfcd,#9c9a97)"></div>
  <div class="team-name">MARTIN BROWN</div><div class="team-role">Layer</div>
  <div class="team-links"><span><svg width="8" height="6" viewBox="0 0 8 6"><rect width="8" height="6" fill="#fff"/><path d="M0 0l4 3 4-3" stroke="#b4bac0" fill="none"/></svg></span><span></span><span></span></div>
</div>

<div class="abs rule"></div>

<h3 class="abs section-title" style="left:56px">Testimonials</h3>
<div class="abs quote-link"><svg width="9" height="9" viewBox="0 0 9 9"><path d="M3.5 5.5l2-2M2.5 4L1.3 5.2a1.6 1.6 0 002.3 2.3L4.8 6.3M6.5 5l1.2-1.2a1.6 1.6 0 00-2.3-2.3L4.2 2.7" stroke="#555" fill="none" stroke-width="1"/></svg></div>
<div class="abs quote">laboris nisi ut aliquip ex commodo consequat Duis aute irure dolor in reprehenderit in voluptate velit esse cillum dolore eu fugiat nulla [...]</div>
<div class="abs quote-tail"></div>
<div class="abs client-photo" role="img" aria-label="Client portrait"></div>
<div class="abs client-name">BIL BLACK</div>
<div class="abs client-org">Company</div>
<div class="abs quote-arrows">
  <span><svg width="5" height="8" viewBox="0 0 5 8"><path d="M4.5 .5L1 4l3.5 3.5" stroke="#444" fill="none"/></svg></span>
  <span><svg width="5" height="8" viewBox="0 0 5 8"><path d="M.5 .5L4 4 .5 7.5" stroke="#444" fill="none"/></svg></span>
</div>

<h3 class="abs section-title" style="left:269px">Contacy</h3>
<div class="abs contact-row" style="top:921px"><div class="contact-icon"><svg width="10" height="13" viewBox="0 0 10 13"><path d="M5 0a4.5 4.5 0 00-4.5 4.5C.5 8 5 13 5 13s4.5-5 4.5-8.5A4.5 4.5 0 005 0z" fill="#fff"/><circle cx="5" cy="4.5" r="1.6" fill="#c9ced3"/></svg></div><span style="padding-top:2px">Adress adress adress</span></div>
<div class="abs contact-row" style="top:955px"><div class="contact-icon"><svg width="11" height="11" viewBox="0 0 11 11"><path d="M2 0l2 2.5-1.2 1.5a7 7 0 004 4L8.5 6.8 11 9 9.5 11C4.5 10.5.5 6.5 0 1.5z" fill="#fff"/></svg></div><span style="padding-top:9px">358-4170926</span></div>
<div class="abs contact-row" style="top:987px"><div class="contact-icon"><svg width="12" height="11" viewBox="0 0 12 11"><rect x="3" y="0" width="6" height="3" fill="#fff"/><rect x="0" y="3.5" width="12" height="5" fill="#fff"/><rect x="3" y="7" width="6" height="4" fill="#fff" stroke="#c9ced3"/></svg></div><span style="padding-top:9px">358-4170926</span></div>
<div class="abs contact-row" style="top:1019px"><div class="contact-icon"><svg width="12" height="9" viewBox="0 0 12 9"><rect width="12" height="9" fill="#fff"/><path d="M0 0l6 5 6-5" stroke="#c9ced3" fill="none"/></svg></div><span style="padding-top:9px">desk@cedarbight.lawyer</span></div>

<h3 class="abs section-title" style="left:483px">Conatctform</h3>
<div class="abs field" style="top:921px">Your name</div>
<div class="abs field" style="top:947px">Your e-mail</div>
<div class="abs field" style="top:973px">Subject</div>
<div class="abs message-box"></div>
<div class="abs send-btn">Send message</div>

<footer class="abs site-footer"></footer>
<div class="abs footer-rule"></div>
<div class="abs copyright">© 2016 Homepage. All Rights Reserved.</div>
<div class="abs social-dot" style="left:649px;top:1172px;background:#4f5b6b"></div>
<div class="abs social-dot" style="left:668px;top:1172px;background:#4f5b6b"></div>

</body>
</html>
```